Gentle Brook toothpaste tube design

Design a Gentle Brook tube design for our all natural toothpaste. The toothpaste is 100% natural with a smooth marshmallow consistency. It's unique because it's not pastelike at all. The all natural flavors make the toothpaste taste great. The toothpaste is smooth yet still leaves your mouth feeling squeaky clean. We want to market this as an all natural family toothpaste.

The flavor is Mint. (possibly called "Cozy Mint")

We have included our logo (eps & jpg), information that goes on the back of the tube, and the artwork template from the tube supplier for the 4.2oz tube.

We like a vintage earthy retro look and feel but we are not limited to this.

The tubes stand upright as shown in the picture of File 4.
Updates

The finished artwork must include anĀ adobe illustratorĀ file.

Project Deadline Extended

I would like to thank all of the designers for their work on this project. We had a difficult time making a decision since all of the designs were very close to what we expected.

Sincerely,

Wes

Target Market(s)

The target market is families that desire an all natural toothpaste. We will be stressing the 100% natural and great taste.

Requirements
Must have
• Three colors maximum due to tube manufacture restrictions.

Must have "100% natural" and "fluoride free" on front of tube. A reference to the great taste or flavor is also important.

Must say 4.2 oz on the front of the tube, centered, at the bottom.
Nice to have
• Fun, colorful packaging that will stand out. Go to your local store and stand in front of the tootpaste shelves, give us something different!
Should not have
• We do not want a lot of red or blue because these are predominate colors already in use on toothpaste tubes and boxes.

```html
<!DOCTYPE html>
<html lang="en">
<head>
<meta charset="utf-8">
<title>Gentle Brook – Cozy Mint tube range</title>
<link rel="stylesheet" href="https://fonts.googleapis.com/css2?family=Cabin:ital,wght@0,400;0,600;0,700;1,400;1,600;1,700&display=swap">
<style>
  :root{
    --backdrop-top:#e4e6e6;
    --backdrop-bottom:#fafafa;
    --tube-white:#f7f6f1;
    --tube-shade:#e7e5dd;
    --cap-white:#f1f0ea;
    --leaf-green:#23822f;
    --deep-green:#0e5a22;
    --ink:#333333;
    --band-mint:#2b8a2a;
    --band-berry:#c22448;
    --band-sun:#f0a818;
    --sky-dark:#0a5f98;
    --sky-mid:#2a9cc4;
    --sky-light:#bfe3ea;
    --teal-dark:#0a4f5c;
    --teal-mid:#23868a;
    --teal-light:#9fd3cf;
    --forest-dark:#0b5e26;
    --forest-mid:#3c9e36;
    --forest-light:#b9df8a;
  }
  *{box-sizing:border-box;margin:0;padding:0}
  html,body{width:1200px;height:1200px;overflow:hidden}
  body{
    background:radial-gradient(ellipse at 50% 25%,var(--backdrop-bottom) 0%,var(--backdrop-top) 100%);
    font-family:"Cabin",sans-serif;
    position:relative;
  }
  .tube{position:absolute;}
  .tube__body{
    position:absolute;left:0;right:0;top:0;bottom:4.4em;
    background:linear-gradient(90deg,var(--tube-shade) 0%,var(--tube-white) 18%,var(--tube-white) 82%,var(--tube-shade) 100%);
    border-radius:0.3em 0.3em 1.6em 1.6em;
    overflow:hidden;
    text-align:center;
  }
  .tube__crimp{
    position:absolute;left:0;right:0;top:0;height:1.1em;
    background:repeating-linear-gradient(90deg,#ecebe4 0 0.25em,#f9f8f4 0.25em 0.5em);
    border-bottom:1px solid #dcdad2;
  }
  .tube__art{position:absolute;left:0;right:0;top:1.1em;height:10.6em}
  .tube--sky .tube__art{background:linear-gradient(160deg,var(--sky-dark) 0%,var(--sky-mid) 55%,var(--sky-light) 100%)}
  .tube--teal .tube__art{background:linear-gradient(160deg,var(--teal-dark) 0%,var(--teal-mid) 60%,var(--teal-light) 100%)}
  .tube--forest .tube__art{background:linear-gradient(160deg,var(--forest-dark) 0%,var(--forest-mid) 55%,var(--forest-light) 100%)}
  .tube__cap{
    position:absolute;bottom:0;left:20%;right:20%;height:4.8em;
    background:linear-gradient(90deg,#e2e0d8 0%,var(--cap-white) 25%,var(--cap-white) 75%,#e2e0d8 100%);
    border-radius:0.3em 0.3em 0.5em 0.5em;
    border-top:2px solid #dddbd2;
  }
  .brand{
    position:absolute;left:50%;top:8.6em;transform:translateX(-50%);
    display:flex;align-items:center;gap:0.35em;
    background:var(--tube-white);padding:0.45em 0.8em;border-radius:2em;
    white-space:nowrap;
  }
  .brand__dot{width:0.8em;height:0.8em;border-radius:50%;background:var(--leaf-green);flex:none}
  .brand__name{font-weight:700;font-size:1.45em;color:var(--leaf-green);line-height:1}
  .front-copy{position:absolute;left:0;right:0;top:13.6em}
  .front-copy__product{font-size:0.75em;color:var(--ink);letter-spacing:0.02em}
  .front-copy__product b{font-weight:400;font-size:1.45em;color:var(--leaf-green);font-style:italic}
  .front-copy__claim{font-style:italic;font-size:1.2em;color:var(--ink);margin-top:0.15em}
  .flavor-band{
    margin:0.35em auto 0;width:84%;
    font-weight:700;font-size:1.3em;color:#fff;letter-spacing:0.03em;
    padding:0.08em 0 0.12em;line-height:1.15;
  }
  .tube--sky .flavor-band{background:var(--band-mint)}
  .tube--teal .flavor-band{background:var(--band-berry)}
  .tube--forest .flavor-band{background:linear-gradient(90deg,var(--band-sun),#f6c33a)}
  .front-copy__free{font-weight:700;font-style:italic;font-size:1.25em;color:var(--deep-green);margin-top:0.2em}
  .front-copy__texture{font-size:0.5em;color:var(--ink);margin-top:0.2em}
  .front-copy__weight{font-size:0.42em;color:#777;margin-top:1.2em;letter-spacing:0.05em}
  .back-copy{
    position:absolute;left:0.9em;right:0.9em;top:4.6em;
    text-align:left;font-size:0.46em;line-height:1.35;color:#444;
  }
  .back-copy p{margin-bottom:1.9em}
  .back-copy strong{color:#222}
  .back-copy__maker{font-size:0.9em}
  .recycle{position:absolute;left:50%;top:32.5em;transform:translateX(-50%);text-align:center;color:#555}
  .recycle svg{display:block;margin:0 auto;width:1.4em;height:1.4em}
  .recycle span{font-size:0.4em}
</style>
</head>
<body>

  <div class="tube tube--sky" style="left:120px;top:400px;width:230px;height:600px;font-size:16px">
    <div class="tube__body">
      <div class="tube__crimp"></div>
      <div class="tube__art" role="img" aria-label="Blue sky artwork with soft light sparkles"></div>
      <div class="brand"><span class="brand__dot"></span><span class="brand__name">Gentle Brook</span></div>
      <div class="front-copy">
        <p class="front-copy__product">dental <b>cream</b></p>
        <p class="front-copy__claim">100% natural</p>
        <p class="flavor-band">cozy mint</p>
        <p class="front-copy__free">fluoride free!</p>
        <p class="front-copy__texture">with a smooth marshmallow consistency</p>
        <p class="front-copy__weight">NET WT. 4.2 oz</p>
      </div>
    </div>
    <div class="tube__cap"></div>
  </div>

  <div class="tube tube--teal" style="left:380px;top:440px;width:200px;height:545px;font-size:13.9px">
    <div class="tube__body">
      <div class="tube__crimp"></div>
      <div class="tube__art" role="img" aria-label="Teal water artwork with soft light sparkles"></div>
      <div class="brand"><span class="brand__dot"></span><span class="brand__name">Gentle Brook</span></div>
      <div class="front-copy">
        <p class="front-copy__product">dental <b>cream</b></p>
        <p class="front-copy__claim">100% natural</p>
        <p class="flavor-band">cozy mint</p>
        <p class="front-copy__free">fluoride free!</p>
        <p class="front-copy__texture">with a smooth marshmallow consistency</p>
        <p class="front-copy__weight">NET WT. 4.2 oz</p>
      </div>
    </div>
    <div class="tube__cap"></div>
  </div>

  <div class="tube tube--forest" style="left:610px;top:385px;width:240px;height:620px;font-size:16.7px">
    <div class="tube__body">
      <div class="tube__crimp"></div>
      <div class="tube__art" role="img" aria-label="Green leafy artwork with soft light sparkles"></div>
      <div class="brand"><span class="brand__dot"></span><span class="brand__name">Gentle Brook</span></div>
      <div class="front-copy">
        <p class="front-copy__product">dental <b>cream</b></p>
        <p class="front-copy__claim">100% natural</p>
        <p class="flavor-band">cozy mint</p>
        <p class="front-copy__free">fluoride free!</p>
        <p class="front-copy__texture">with a smooth marshmallow consistency</p>
        <p class="front-copy__weight">NET WT. 4.2 oz</p>
      </div>
    </div>
    <div class="tube__cap"></div>
  </div>

  <div class="tube tube--back" style="left:880px;top:440px;width:200px;height:545px;font-size:13.9px">
    <div class="tube__body">
      <div class="tube__crimp"></div>
      <div class="back-copy">
        <p><strong>Directions:</strong> Adults and children 2 years of age and older: Brush teeth thoroughly, preferably after each meal or at least twice a day, or as directed by a dentist. <strong>Children under 2 years:</strong> consult a dentist.</p>
        <p><strong>Natural ingredients:</strong> vegetable glycerin, deionized water, xylitol, sodium bicarbonate, USDA organic flavor, spearmint oil, sodium coco-sulfate (derived from coconut oil) and carrageenan (extracted from seaweed).</p>
        <p><strong>No parabens</strong>, no gluten, no SLS, no TEA, no formaldehyde, no artificial flavors, no artificial dye, no artificial sweetener, no dairy, no sorbitol, no saccharin, no peroxide, and no fluoride!</p>
        <p class="back-copy__maker">Made in USA.<br>Distributed &amp; Bottled by:<br>Gentle Brook LLC, 120 Willow Lane, Fairview, OR 97000<br>www.gentlebrook.com<br>info@gentlebrook.com</p>
      </div>
      <div class="recycle">
        <svg viewBox="0 0 24 24" fill="none" stroke="#3a7ca5" stroke-width="2" stroke-linecap="round" stroke-linejoin="round" aria-hidden="true">
          <path d="M20 12a8 8 0 1 1-3-6.2"/>
          <path d="M17 2v4h4"/>
        </svg>
        <span>Recycle</span>
      </div>
    </div>
    <div class="tube__cap"></div>
  </div>

</body>
</html>
```